Gavin Holloway Advisory - Web Design Project

We need a web design for my new edgy consulting business specializing in innovation, technology and strategy.

It is our personal goal to turn each client into raving fans by helping them achieve their own business goals and aspirations through assisting them in raising their own innovation and marketing standards.

We provide our personalised and state-of-the-art services to our clients and boards who represent some of the world greatest innovative thinkers.

Here is some other information which may help shape your thinking.

I've had direct Involvement in the development of the following iPad, iPhone Applications and websites

PelicanTrailsHub.com (TerraLoom platform) by Coastline Visitor Bureau
http://pelicantrailshub.example

Harbor Zest by Tidy Sailways
https://apps.example.net/au/app/harbor-zest/id900111222

RedDustGo by Frontier Visits Office
https://apps.example.net/au/app/reddustgo/id900111333

Wexbridge Rambles
http://www.wexbridgerambles.example

Trip Weaver by Coastline Visitor Bureau
http://apps.example.net/au/app/trip-weaver/id900111444

Sunward by Sunward Travel Board
https://apps.example.net/au/app/sunward/id900111555

Fernvale Ridge Road Loop by Roamwell Agency
https://apps.example.net/au/app/fernvale-ridge-road-loop/id900111666

Pathfinder Run by Frontier Visits Office and Southern Coast Visitor Council
https://apps.example.net/au/app/pathfinder-run-grand-trek/id900111777

Gavin Holloway Advisory (GHA)
November 2012 – Present (8 months)Brisbane, Sydney, Canberra

Gavin’s consults to Small-to-Medium Enterprises (SME) and Government organisations on business strategy, technology strategy, risk mitigation, disruptive technology and innovation in the workplace.

Gavin’s consultancy mantra is that we cannot divorce economic life from cultural life particularly in an era when social capital may be as important as physical capital in business.

Reason: request from designers, I want to see their best efforts

Target Market(s)

35+

Industry/Entity Type

Business

Requirements
Must have
• Please use some of the personal image(s) contained in the zip files which can be downloaded from here

http://filedrop.example/k7Pq2Lm9
http://filedrop.example/r4Tz8Hv1
http://filedrop.example/w6Nc3Bx5
Nice to have
• Black, Sleek design, maybe minimalist. Nice to have a Glint for the design. Nice to have it easily ported to Wordpress or be a modified Wordpress template. HTML 5, responsive design

```html
<!DOCTYPE html>
<html lang="en">
<head>
<meta charset="utf-8">
<title>Gavin Holloway Advisory</title>
<link rel="stylesheet" href="https://fonts.googleapis.com/css2?family=Oswald:wght@500;600&family=Roboto+Condensed:wght@300;400;700&display=swap">
<style>
  :root {
    --sky-light: #c9bcc4;
    --sky-mid: #8f8398;
    --city-mid: #4e4c70;
    --city-dark: #24233d;
    --text-white: #ffffff;
    --accent-blue: #2f8ae0;
    --button-top: #3fa0f0;
    --button-bottom: #1f6fc8;
    --button-frame: rgba(40, 40, 70, 0.55);
  }
  * { margin: 0; padding: 0; box-sizing: border-box; }
  html, body {
    width: 1200px;
    height: 800px;
    overflow: hidden;
    background: var(--city-dark);
  }
  .hero {
    position: relative;
    width: 1200px;
    height: 800px;
    overflow: hidden;
  }
  .hero-backdrop {
    position: absolute;
    inset: 0;
    background:
      radial-gradient(ellipse 70% 60% at 50% 55%, rgba(255,255,255,0.08), rgba(0,0,0,0) 70%),
      radial-gradient(ellipse 120% 90% at 50% 50%, rgba(0,0,0,0) 55%, rgba(15,12,35,0.55) 100%),
      linear-gradient(180deg,
        var(--sky-light) 0%,
        var(--sky-mid) 9%,
        #6e6580 14%,
        var(--city-mid) 30%,
        #5b5a7c 55%,
        #3c3b5c 80%,
        var(--city-dark) 100%);
  }
  .hero-content {
    position: absolute;
    inset: 0;
    text-align: center;
    color: var(--text-white);
  }
  .brand-title {
    position: absolute;
    top: 198px;
    left: 0;
    right: 0;
    font-family: 'Oswald', sans-serif;
    font-weight: 600;
    font-size: 64px;
    line-height: 80px;
    letter-spacing: -0.5px;
  }
  .brand-title .accent { color: var(--accent-blue); }
  .mantra {
    position: absolute;
    top: 315px;
    left: 0;
    right: 0;
    font-family: 'Roboto Condensed', sans-serif;
    font-weight: 300;
    font-size: 36px;
    line-height: 52px;
  }
  .cta-frame {
    position: absolute;
    left: 478px;
    top: 541px;
    width: 255px;
    height: 74px;
    border-radius: 6px;
    background: var(--button-frame);
    padding: 8px 9px;
  }
  .cta-button {
    display: flex;
    align-items: center;
    justify-content: center;
    gap: 10px;
    width: 100%;
    height: 100%;
    border-radius: 4px;
    background: linear-gradient(180deg, var(--button-top), var(--button-bottom));
    color: var(--text-white);
    text-decoration: none;
    font-family: 'Roboto Condensed', sans-serif;
    font-size: 30px;
    letter-spacing: 0.3px;
  }
  .cta-button .light { font-weight: 300; }
  .cta-button .bold { font-weight: 700; margin-left: -2px; }
  .cta-button svg { width: 12px; height: 16px; }
</style>
</head>
<body>
  <main class="hero">
    <div class="hero-backdrop" role="img" aria-label="Soft-focus aerial photograph of a city skyline with high-rise towers under a hazy sky"></div>
    <div class="hero-content">
      <h1 class="brand-title">Gavin Holloway <span class="accent">Advisory</span></h1>
      <p class="mantra">We cannot divorce economic life from cultural life<br>particularly in an era when social capital may be as important<br>as physical capital in business.</p>
      <div class="cta-frame">
        <a class="cta-button" href="#">
          <span><span class="light">GET</span> <span class="bold">INNOVATIVE</span></span>
          <svg viewBox="0 0 12 16" aria-hidden="true"><path d="M3 3 L8 8 L3 13" fill="none" stroke="#ffffff" stroke-width="2.6"/></svg>
        </a>
      </div>
    </div>
  </main>
</body>
</html>
```